Indoor location business needs re-design two websites (one website and one back office)

We are a company active in the indoor location and navigation industry. We are developing software and SDKs.
We are looking for someone who will re-design two of our websites.
Color and style have to become similar and the design as to be improved.
The first:
https://indoor.brelvanto.com
You will find all the content attached
The second
https://indoor.brelvanto.com/indoor/admin/
Here are credentials for this one.
Account: design
password: quilt475
You will find directly the content on the page.
Target Market(s)
hospital, airport, event organization, retail, museum
Industry/Entity Type
Business
Number of Pages Required
5+ page
Requirements
Must have
- The contain that are on each page of both websites.

```html
<!DOCTYPE html>
<html lang="en">
<head>
<meta charset="utf-8">
<title>Brelvanto – Indoor Location Technology</title>
<link rel="stylesheet" href="https://fonts.googleapis.com/css2?family=Open+Sans:wght@300;400;600;700&display=swap">
<style>
:root{
  --blue:#1aa3e0;
  --blue-dark:#1283bd;
  --blue-light:#3db8ea;
  --ink:#444;
  --muted:#8a8a8a;
  --nav:#4b4b4b;
  --footer:#3e3e3e;
  --footer-line:#555;
  --light:#f3f3f3;
  --white:#fff;
  --topbar:#f7f7ef;
}
*{box-sizing:border-box;margin:0;padding:0}
html,body{width:1200px;height:3042px;overflow:hidden}
body{font-family:"Open Sans",Arial,sans-serif;color:var(--ink);background:var(--white);position:relative}
.wrap{width:950px;margin:0 auto;position:relative;height:100%}
section,header,footer,nav{position:relative;width:1200px}
.btn{display:inline-block;background:var(--blue);color:var(--white);font-size:12px;padding:0 18px;height:34px;line-height:34px;text-align:center}
.btn-ghost{border:1px solid var(--white);background:transparent}

/* top bar */
.topbar{height:27px;background:var(--topbar)}
.socials{position:absolute;left:0;top:6px;display:flex;gap:3px}
.socials span{width:15px;height:15px;display:block}
.topbar .lang{position:absolute;right:0;top:6px;font-size:10px;color:var(--muted);display:flex;gap:8px;align-items:center}
.topbar .lang b{font-weight:400;border:1px solid #ddd;background:#fff;padding:0 14px;height:15px;line-height:13px}

/* header */
.header{height:91px;background:var(--white)}
.logo{position:absolute;left:0;top:14px;display:flex;align-items:center;gap:10px}
.logo i{width:56px;height:56px;border-radius:50%;background:var(--blue);display:block}
.logo span{font-size:22px;font-weight:700;color:var(--blue)}
.search{position:absolute;left:240px;top:36px;width:470px;border-bottom:1px solid #e2e2e2;height:22px;font-size:11px;color:#bbb}
.search svg{position:absolute;right:4px;top:4px}
.auth{position:absolute;right:0;top:36px;display:flex;gap:8px}
.auth span{height:22px;line-height:22px;font-size:10px;padding:0 16px}
.auth .login{background:#e9e9e9;color:var(--muted)}
.auth .register{background:var(--blue);color:#fff}

/* nav */
.mainnav{height:27px;background:var(--nav)}
.mainnav ul{list-style:none;display:flex;height:27px}
.mainnav li{color:#ddd;font-size:10px;line-height:27px;padding:0 21px;text-transform:uppercase}
.mainnav li.active{background:var(--blue);color:#fff;padding:0 28px}

/* hero */
.hero{height:362px;background:linear-gradient(120deg,#0f6fa3 0%,#1a9ad6 45%,#4cc1ee 100%);color:#fff;overflow:hidden}
.hero h1{position:absolute;left:0;top:88px;font-size:44px;font-weight:400;line-height:50px;width:420px}
.hero p{position:absolute;left:0;top:190px;width:390px;font-size:11px;line-height:16px;color:#e6f5fc}
.hero .btn{position:absolute;left:0;top:230px;height:30px;line-height:28px;font-size:11px}
.laptop{position:absolute;left:570px;top:45px;width:330px;height:225px}
.laptop .screen{position:absolute;left:35px;top:0;width:260px;height:180px;background:#222;border-radius:8px;padding:9px}
.laptop .screen div{width:100%;height:100%;background:linear-gradient(135deg,#7b8a98,#c8ccd1 50%,#5b6978)}
.laptop .base{position:absolute;left:0;top:180px;width:330px;height:14px;background:linear-gradient(#e6e6e6,#9a9a9a);border-radius:0 0 40px 40px}
.arrow{position:absolute;top:165px;width:22px;height:22px;border-radius:50%;background:rgba(255,255,255,.85)}
.arrow.l{left:-30px}.arrow.r{right:-30px}
.dots{position:absolute;left:50%;bottom:30px;transform:translateX(-50%);display:flex;gap:6px}
.dots i{width:7px;height:7px;border-radius:50%;background:rgba(255,255,255,.5)}
.dots i:first-child{background:#fff}

/* tagline */
.tagline{height:135px;text-align:center;display:flex;align-items:center;justify-content:center}
.tagline h2{font-size:27px;font-weight:400;line-height:40px;color:var(--blue);width:720px}

/* video */
.video{height:438px;background:var(--light)}
.player{position:absolute;left:0;top:52px;width:694px;height:338px;background:linear-gradient(135deg,#3c3c3c,#7d7d7d 50%,#2e2e2e)}
.player .play{position:absolute;left:50%;top:50%;transform:translate(-50%,-50%)}
.player .step{position:absolute;right:40px;top:10px;color:#fff;font-size:26px;font-weight:700}
.player .topstrip{position:absolute;left:0;top:0;width:100%;height:22px;background:rgba(255,255,255,.18)}

/* partners */
.partners{height:272px}
.partners h3{position:absolute;left:0;top:40px;font-size:16px;font-weight:700;color:var(--blue);border-bottom:2px solid var(--blue);padding-bottom:2px}
.partners h3 span{font-weight:400;color:var(--ink)}
.partner-row{position:absolute;left:0;display:flex;justify-content:space-between;width:690px}
.partner-row.r1{top:100px}.partner-row.r2{top:170px}
.partner-row span{display:block;height:44px;width:130px;background:#e3e3e3;border-radius:3px}
.partner-row.r2 span:nth-child(1){background:#f36f6a;border-radius:12px}
.partner-row.r2 span:nth-child(2){background:#ef8b8b;width:200px}
.partner-row.r2 span:nth-child(3){background:#3a3a3a;width:190px}

/* feature blocks */
.feature{overflow:hidden}
.feature h3{font-size:18px;font-weight:700;letter-spacing:.5px;text-transform:uppercase;padding-bottom:4px;display:inline-block}
.feature h3 span{font-weight:300}
.feature p{font-size:11px;line-height:16px;margin-top:12px}
.monitor{position:absolute;width:280px;height:235px}
.monitor .scr{width:280px;height:175px;background:#222;border-radius:5px;padding:7px}
.monitor .scr div{width:100%;height:100%}
.monitor .stand{width:60px;height:30px;margin:0 auto;background:linear-gradient(#ccc,#eaeaea)}
.monitor .foot{width:110px;height:8px;margin:0 auto;background:#d8d8d8;border-radius:3px}

.geo{height:388px;background:var(--blue);color:#fff}
.geo .shadow{position:absolute;left:640px;top:150px;width:1200px;height:800px;background:var(--blue-dark);transform:rotate(45deg);transform-origin:0 0;opacity:.55}
.geo .text{position:absolute;left:0;top:90px;width:340px}
.geo h3{border-bottom:2px solid #fff}
.geo .btns{display:flex;gap:14px;margin-top:28px}
.geo .btns .btn{background:transparent;border:1px solid #fff;width:160px;font-size:11px}
.geo .monitor{left:640px;top:80px}
.geo .monitor .scr div{background:linear-gradient(135deg,#fff 0%,#f2f2f2 60%,#e8e8e8)}

.navi{height:356px;background:#fff}
.navi .phone{position:absolute;left:0;top:85px;width:250px;height:150px;border-radius:26px;background:linear-gradient(160deg,#fdfdfd,#d7d7d7);transform:rotate(18deg);box-shadow:0 8px 20px rgba(0,0,0,.1)}
.navi .phone div{position:absolute;left:30px;top:12px;width:190px;height:126px;background:linear-gradient(135deg,#f1f1f1,#dcdcdc)}
.navi .text{position:absolute;left:400px;top:80px;width:420px}
.navi h3{color:var(--blue);border-bottom:2px solid var(--blue)}
.navi p{color:var(--blue)}
.navi .btns{display:flex;gap:10px;margin-top:40px}
.navi .btns .btn{width:165px;font-size:10px}

.data{height:372px;background:var(--light)}
.data .shadow{position:absolute;left:660px;top:170px;width:1200px;height:800px;background:#e4e4e4;transform:rotate(45deg);transform-origin:0 0}
.data .text{position:absolute;left:0;top:60px;width:330px}
.data h3{color:var(--blue);border-bottom:2px solid var(--blue)}
.data h3 span{color:var(--ink)}
.data p{color:var(--muted)}
.data .btns{display:flex;gap:12px;margin-top:34px}
.data .btns .btn{width:105px}
.data .monitor{left:640px;top:55px}
.data .monitor .scr div{background:#fff;position:relative}

/* signup */
.signup{height:219px;text-align:center}
.signup h2{font-size:27px;font-weight:400;line-height:40px;color:var(--blue);width:720px;margin:36px auto 0}
.signup p{font-size:14px;color:var(--muted);margin-top:12px}
.signup .field{width:180px;margin:14px auto 0;border-bottom:1px solid #ddd;height:22px;font-size:10px;color:#bbb;line-height:22px}
.signup .btn{margin-top:14px;height:28px;line-height:28px;width:110px;font-size:11px}

/* footer */
.footer{height:355px;background:var(--footer);color:#bbb}
.footer .col{position:absolute;top:30px;font-size:10px}
.footer h4{font-size:13px;font-weight:400;color:#ddd;text-transform:uppercase;border-bottom:1px solid var(--footer-line);padding-bottom:6px;margin-bottom:14px}
.sitemap{left:0;width:250px}
.sitemap ul{list-style:none;display:grid;grid-template-columns:1fr 1fr;row-gap:12px}
.posts{left:175px;width:165px}
.posts .post{margin-bottom:12px;line-height:13px}
.posts .post b{display:block;font-weight:600;color:#ddd}
.contact{left:360px;width:290px}
.contact .row{display:flex;gap:12px;align-items:flex-start;margin-bottom:14px;line-height:13px}
.contact .ico{width:18px;flex:none}
.fsoc{display:flex;gap:3px}
.fsoc span{width:18px;height:18px;display:block}
.flogo{position:absolute;left:810px;top:40px;display:flex;align-items:center;gap:10px}
.flogo i{width:90px;height:90px;border-radius:50%;background:#5a5a5a;display:block}
.flogo span{font-size:18px;font-weight:700;color:#6d6d6d}
.footer .bottom{position:absolute;left:0;right:0;top:318px;border-top:1px solid var(--footer-line);padding-top:8px;font-size:9px;text-align:center;color:#999}
.footer .bottom span{position:absolute;right:0;top:8px}
</style>
</head>
<body>

<div class="topbar"><div class="wrap">
  <div class="socials">
    <span style="background:#3b5998"></span><span style="background:#1da1f2"></span><span style="background:#dd4b39"></span><span style="background:#0077b5"></span><span style="background:#e4405f"></span><span style="background:#f57d00"></span>
  </div>
  <div class="lang">Follow us today <b>English</b></div>
</div></div>

<header class="header"><div class="wrap">
  <div class="logo"><i></i><span>Brelvanto</span></div>
  <div class="search">Search
    <svg width="12" height="12" viewBox="0 0 12 12"><circle cx="5" cy="5" r="3.5" fill="none" stroke="#aaa" stroke-width="1.5"/><line x1="7.6" y1="7.6" x2="11" y2="11" stroke="#aaa" stroke-width="1.5"/></svg>
  </div>
  <div class="auth"><span class="login">Login</span><span class="register">Register</span></div>
</div></header>

<nav class="mainnav"><div class="wrap">
  <ul><li class="active">Home</li><li>Use cases</li><li>Prices</li><li>Free trial</li><li>SDK zone</li><li>About</li><li>Contact</li><li>More</li></ul>
</div></nav>

<section class="hero"><div class="wrap">
  <div class="arrow l"></div><div class="arrow r"></div>
  <h1>Indoor Location Technology</h1>
  <p>Use our platform and sets of SDKs to access additional indoor features: Navigation, Data Analysis, Geofencing and Notifications.</p>
  <span class="btn btn-ghost">Free Trial</span>
  <div class="laptop">
    <div class="screen"><div role="img" aria-label="Laptop showing people walking through a busy shopping mall"></div></div>
    <div class="base"></div>
  </div>
  <div class="dots"><i></i><i></i><i></i></div>
</div></section>

<section class="tagline"><h2>Set up 10'000 m2 in 4 hours and reach an accuracy of 2 meters in only 3 steps!</h2></section>

<section class="video"><div class="wrap">
  <div class="player" role="img" aria-label="Video preview of the indoor mapping tool at step two, floor plan and aerial map">
    <div class="topstrip"></div>
    <div class="step">Step 2</div>
    <svg class="play" width="40" height="44" viewBox="0 0 40 44"><polygon points="4,2 38,22 4,42" fill="#fff"/></svg>
  </div>
</div></section>

<section class="partners"><div class="wrap">
  <h3>THEY <span>TRUST US</span></h3>
  <div class="partner-row r1"><span></span><span></span><span></span><span></span></div>
  <div class="partner-row r2"><span></span><span></span><span></span></div>
</div></section>

<section class="feature geo">
  <div class="shadow"></div>
  <div class="wrap">
    <div class="text">
      <h3>Geofencing <span>&amp; Notifications</span></h3>
      <p>Quickly import, position and manage your floor plans. Create points of interest and geozones to deploy push notifications in your app and get statistics on specific areas.</p>
      <div class="btns"><span class="btn">Geo map engine</span><span class="btn">Push notification</span></div>
    </div>
    <div class="monitor"><div class="scr"><div role="img" aria-label="Monitor showing the geofencing dashboard with a floor plan"></div></div><div class="stand"></div><div class="foot"></div></div>
  </div>
</section>

<section class="feature navi"><div class="wrap">
  <div class="phone"><div role="img" aria-label="Smartphone showing an indoor route on a map"></div></div>
  <div class="text">
    <h3>Navigation</h3>
    <p>By placing beacons, visitors can see themselves on a map of the indoor environment, allowing you to guide them through routes towards each destination.</p>
    <div class="btns"><span class="btn">Discover indoor Navigation engine</span><span class="btn">Use along their routes on maps</span></div>
  </div>
</div></section>

<section class="feature data">
  <div class="shadow"></div>
  <div class="wrap">
    <div class="text">
      <h3>Data <span>Analysis</span></h3>
      <p>To help you use all the beacon data you can now see who your visitors are, their frequent areas and when they interact with your venue, thanks to our tools.</p>
      <div class="btns"><span class="btn">Who</span><span class="btn">When</span><span class="btn">Where</span></div>
    </div>
    <div class="monitor"><div class="scr"><div>
      <svg width="266" height="161" viewBox="0 0 266 161">
        <rect x="0" y="0" width="266" height="12" fill="#ececec"/>
        <g fill="#1aa3e0"><rect x="14" y="100" width="8" height="40"/><rect x="28" y="85" width="8" height="55"/><rect x="42" y="110" width="8" height="30"/><rect x="56" y="75" width="8" height="65"/><rect x="70" y="95" width="8" height="45"/></g>
        <polyline points="100,120 120,100 140,110 160,80 180,92" fill="none" stroke="#f0a23b" stroke-width="2"/>
        <circle cx="225" cy="95" r="26" fill="#f36f6a"/>
        <path d="M225 95 L225 69 A26 26 0 0 1 251 95 Z" fill="#1aa3e0"/>
        <path d="M225 95 L251 95 A26 26 0 0 1 210 116 Z" fill="#f5c342"/>
        <circle cx="225" cy="95" r="12" fill="#fff"/>
      </svg>
    </div></div><div class="stand"></div><div class="foot"></div></div>
  </div>
</section>

<section class="signup">
  <h2>Set up 10'000 m2 in 4 hours and reach an accuracy of 2 meters in only 3 steps!</h2>
  <p>If you are interested enter your email address</p>
  <div class="field">Email</div>
  <span class="btn">Submit</span>
</section>

<footer class="footer"><div class="wrap">
  <div class="col sitemap">
    <h4>Sitemap</h4>
    <ul><li>Home</li><li>SDK Zone</li><li>Use Cases</li><li>About</li><li>Prices</li><li>Contact</li><li>Free Trial</li><li>More</li></ul>
  </div>
  <div class="col posts">
    <h4>Recent posts</h4>
    <div class="post"><b>Beacon indoor navigation: new tools for hospitals</b>A short look at how wards and halls can be mapped.</div>
    <div class="post"><b>Indoor location and navigation with beacons</b>Airports now guide travellers to gates faster.</div>
    <div class="post"><b>How to integrate our indoor location SDK</b>Step by step guide for app developers.</div>
  </div>
  <div class="col contact">
    <h4>Contact</h4>
    <div class="row"><svg class="ico" width="16" height="20" viewBox="0 0 16 20"><path d="M8 0a7 7 0 0 0-7 7c0 5 7 13 7 13s7-8 7-13a7 7 0 0 0-7-7z" fill="#bbb"/><circle cx="8" cy="7" r="2.6" fill="#3e3e3e"/></svg><span>Brelvanto SA<br>Rue des Tilleuls 12, 1204 Genève</span></div>
    <div class="row"><svg class="ico" width="16" height="16" viewBox="0 0 16 16"><path d="M3 1l3 3-2 2c1 2 3 4 5 5l2-2 3 3-2 3C7 15 1 9 1 3z" fill="#bbb"/></svg><span>+41 22 555 01 47</span></div>
    <div class="row"><svg class="ico" width="16" height="12" viewBox="0 0 16 12"><rect x="0" y="0" width="16" height="12" fill="#bbb"/><polyline points="0,0 8,7 16,0" fill="none" stroke="#3e3e3e" stroke-width="1.3"/></svg><span>hello@brelvanto.com</span></div>
    <div class="fsoc"><span style="background:#3b5998"></span><span style="background:#1da1f2"></span><span style="background:#dd4b39"></span><span style="background:#0077b5"></span><span style="background:#e4405f"></span><span style="background:#f57d00"></span><span style="background:#888"></span></div>
  </div>
  <div class="flogo"><i></i><span>Brelvanto</span></div>
  <div class="bottom">© 2015 Brelvanto. All Rights Reserved.<span>Terms &amp; Privacy</span></div>
</div></footer>

</body>
</html>
```